Stylish Business Cards Wanted

- DOUBLE SIDED Design Required -

High end, edgy cards for a corporate and personal stylist. Must include logo,
Name: Belinda Marsh
Title: Director and Stylist
telephone : +61 8 8417 2950
email: belinda@thewardrobeledger.com
website: thewardrobeledger.com
Tag: Corporate Workwear & Uniform Specialist | Personal Stylist
Would like nice icons for telephone, email, website

Target Market(s)

Businesses wanting stylish uniforms, people wanting stylish wardrobes

Industry/Entity Type

Corporate Workwear Stylist

Contact Information for Business Card

I would like black, white and gold foiling incorporated in the design - possibly a touch of the other colours on my branding guide attached Name: Belinda Marsh Title: Director and Stylist telephone : +61 8 8417 2950 email: belinda@thewardrobeledger.com website: thewardrobeledger.com Tag: Corporate Workwear & Uniform Specialist | Personal Stylist Would like nice icons for telephone, email, website

Font styles to use
Other font styles liked:
• Raleway

Colors

Designer to choose colors to be used in the design.

Requirements
Must have
• Gold foil accents

```html
<!DOCTYPE html>
<html lang="en">
<head>
<meta charset="utf-8">
<title>The Wardrobe Ledger – Business Card</title>
<link rel="stylesheet" href="https://fonts.googleapis.com/css2?family=Open+Sans:wght@400;600;700&display=swap">
<style>
  :root {
    --backdrop: #232323;
    --card: #0f0f0f;
    --gold: #cdbb72;
    --gold-soft: #b8a765;
    --gold-light: #f2ebb8;
    --gold-deep: #9e8a45;
    --foil: linear-gradient(100deg, var(--gold-deep) 0%, var(--gold-light) 45%, #d9c98a 60%, var(--gold-deep) 100%);
  }
  * { box-sizing: border-box; margin: 0; padding: 0; }
  html, body {
    width: 1200px; height: 900px; overflow: hidden;
    background: var(--backdrop);
    font-family: "Open Sans", Arial, sans-serif;
  }
  .canvas {
    width: 1200px; height: 900px;
    display: flex; flex-direction: column; align-items: center; justify-content: center; gap: 40px;
  }
  .card {
    position: relative; width: 640px; height: 391px;
    background: var(--card); overflow: hidden;
    box-shadow: 0 10px 30px rgba(0,0,0,.45);
  }
  .card__frame {
    position: absolute; inset: 16px;
    border: 1px solid var(--gold-soft);
  }
  .foil-tab { position: absolute; background: var(--foil); }
  .foil-tab--top { top: 0; height: 40px; border-radius: 0 0 20px 20px; }
  .foil-tab--bottom { bottom: 0; height: 40px; border-radius: 20px 20px 0 0; }
  .foil-tab--left { left: 0; width: 40px; border-radius: 0 20px 20px 0; }
  .foil-tab--right { right: 0; width: 40px; border-radius: 20px 0 0 20px; }

  .brand-name {
    color: var(--gold); font-weight: 700; text-transform: uppercase;
    line-height: 1.1; letter-spacing: .08em;
  }

  /* Contact side */
  .contact .brand-name { position: absolute; left: 44px; top: 150px; width: 200px; font-size: 24px; }
  .contact__divider { position: absolute; left: 262px; top: 130px; width: 1px; height: 160px; background: var(--gold-soft); }
  .contact__details { position: absolute; left: 286px; top: 138px; color: var(--gold); }
  .contact__name { font-size: 23px; font-weight: 700; letter-spacing: .04em; text-transform: uppercase; }
  .contact__title { font-size: 15px; margin-top: 2px; color: var(--gold-soft); }
  .contact__list { list-style: none; margin-top: 22px; }
  .contact__item { display: flex; align-items: center; gap: 9px; font-size: 15px; line-height: 1.6; }
  .contact__icon { width: 14px; height: 14px; flex: none; }

  /* Brand side */
  .brand .brand-name { position: absolute; right: 70px; top: 105px; font-size: 46px; text-align: right; }
  .brand__tagline {
    position: absolute; left: 40px; right: 40px; bottom: 34px;
    color: var(--gold); font-size: 15px; text-align: left;
  }
</style>
</head>
<body>
<main class="canvas">
  <section class="card contact" aria-label="Business card, contact side">
    <div class="card__frame"></div>
    <div class="foil-tab foil-tab--top" style="left:330px;width:240px"></div>
    <div class="foil-tab foil-tab--bottom" style="left:90px;width:250px"></div>
    <p class="brand-name">The Wardrobe Ledger</p>
    <div class="contact__divider"></div>
    <div class="contact__details">
      <h1 class="contact__name">Belinda Marsh</h1>
      <p class="contact__title">Director and Stylist</p>
      <ul class="contact__list">
        <li class="contact__item">
          <svg class="contact__icon" viewBox="0 0 16 16" aria-hidden="true"><circle cx="8" cy="8" r="8" fill="var(--gold)"/><path d="M5.2 4.2l1.6 0 .6 2-1 .8a5 5 0 0 0 2.6 2.6l.8-1 2 .6v1.6c0 .5-.5.9-1 .8A7 7 0 0 1 4.4 5.2c-.1-.5.3-1 .8-1z" fill="var(--card)"/></svg>
          +61 8 8417 2950
        </li>
        <li class="contact__item">
          <svg class="contact__icon" viewBox="0 0 16 16" aria-hidden="true"><rect x="1" y="3.5" width="14" height="9" rx="1" fill="var(--gold)"/><path d="M1.5 4l6.5 5 6.5-5" fill="none" stroke="var(--card)" stroke-width="1.2"/></svg>
          belinda@thewardrobeledger.com
        </li>
        <li class="contact__item">
          <svg class="contact__icon" viewBox="0 0 16 16" aria-hidden="true"><circle cx="8" cy="8" r="7" fill="var(--gold)"/><g fill="none" stroke="var(--card)" stroke-width="1"><ellipse cx="8" cy="8" rx="3" ry="7"/><path d="M1 8h14M2.5 4.5h11M2.5 11.5h11"/></g></svg>
          thewardrobeledger.com
        </li>
      </ul>
    </div>
  </section>

  <section class="card brand" aria-label="Business card, brand side">
    <div class="card__frame"></div>
    <div class="foil-tab foil-tab--left" style="top:30px;height:190px"></div>
    <div class="foil-tab foil-tab--right" style="top:180px;height:190px"></div>
    <p class="brand-name">The Wardrobe<br>Ledger</p>
    <p class="brand__tagline">Corporate Workwear &amp; Uniform Specialist &nbsp;•&nbsp; Personal Stylist</p>
  </section>
</main>
</body>
</html>
```